Pelmora, The winning solution for fundraising

Pelmora needs a simple Wordpress website development. The key message is that we have three wins in fundraising according to my services - win for theorganisation - win for the partner and win for the audience and the community.STYLE:- My business card is attached so the site colors could match with the card;- We love the style of this website: https://www.marnacovestel.co.nz/ because it is modern, minimalist, clean and easy to navigate. I am happy to have a similar parallax (scrolling) site as the reference samplePlease feature the following on the site:* INTRODUCTION (or About)* SERVICES* MY QUOTE* CONTACT US* LINKEDIN ( the contents are in the attached .rtf file - please message me if you are unable to open this document)Deliverables:- I would like a fully functioning (Coded) wordpress site

• Personable approach
• It is all about You (the other person who is approach my business)

```html
<!DOCTYPE html>
<html lang="en">
<head>
<meta charset="utf-8">
<title>Pelmora</title>
<link href="https://fonts.googleapis.com/css2?family=Varela+Round&family=Mulish:wght@400;600;700&family=Nunito:wght@800&display=swap" rel="stylesheet">
<style>
:root{
  --brown:#7b5a4f;
  --rose:#c99c92;
  --rose-light:#d39e93;
  --ink:#2b2b2b;
  --muted:#555;
  --light:#f6f6f6;
  --field:#efefef;
  --dark:#221b1c;
  --white:#fff;
  --circle:#1a6cb5;
}
*{box-sizing:border-box;margin:0;padding:0}
html,body{width:1200px;height:3062px;overflow:hidden}
body{font-family:"Mulish",sans-serif;color:var(--ink);background:var(--white);position:relative}
.heading{font-family:"Varela Round",sans-serif;font-weight:400;color:var(--brown)}
.btn{display:inline-block;background:linear-gradient(90deg,var(--rose),var(--brown));color:var(--white);font-family:"Varela Round",sans-serif;font-size:21px;text-align:center;line-height:52px;height:52px;width:183px}
.circle{display:inline-block;width:36px;height:36px;border-radius:50%;background:var(--circle)}

/* nav */
.nav{position:absolute;top:0;left:0;width:1200px;height:83px;display:flex;align-items:center}
.nav .brand{position:absolute;left:77px;top:14px;font-size:50px;letter-spacing:.5px}
.nav ul{position:absolute;left:533px;top:20px;display:flex;list-style:none;align-items:center}
.nav li{font-size:15px;font-weight:600;letter-spacing:.3px;margin-right:34px;color:var(--ink)}
.nav li.active{background:linear-gradient(90deg,var(--rose),var(--brown));color:var(--white);width:104px;height:47px;line-height:47px;text-align:center;margin-right:28px}
.nav .circle{position:absolute;left:1086px;top:23px}

/* hero */
.hero{position:absolute;top:83px;left:0;width:1200px;height:595px;background:linear-gradient(90deg,#3c3c40 0%,#55555b 45%,#6d6b6c 75%,#4a4748 100%)}
.hero .photo{position:absolute;inset:0;background:radial-gradient(ellipse at 75% 45%,rgba(220,200,185,.35),rgba(0,0,0,0) 55%)}
.hero .rule{position:absolute;left:77px;width:242px;height:1px;background:rgba(255,255,255,.4)}
.hero h1{position:absolute;left:94px;top:209px;font-family:"Nunito",sans-serif;font-size:54px;color:var(--white)}
.hero .creds{position:absolute;left:78px;top:303px;color:var(--white);font-size:18px;word-spacing:2px}
.hero .info{position:absolute;left:79px;color:var(--white);font-size:14px}
.hero .info span{color:var(--rose-light)}

/* about */
.about{position:absolute;top:678px;left:0;width:1200px;height:593px}
.about .band{position:absolute;left:0;top:0;width:479px;height:593px;background:var(--brown)}
.about .portrait{position:absolute;left:0;top:52px;width:426px;height:541px;background:linear-gradient(160deg,#2e5a45 0%,#7d6a50 40%,#c9a07c 70%,#3a2f2b 100%)}
.about h2{position:absolute;left:568px;top:88px;font-size:46px}
.about .lead{position:absolute;left:568px;top:160px;width:560px;font-size:16px;font-weight:700;line-height:27px;color:var(--ink)}
.about .body{position:absolute;left:568px;width:560px;font-size:13.5px;line-height:27px;color:var(--muted)}
.about .btn{position:absolute;left:566px;top:465px}

/* services */
.services{position:absolute;top:1271px;left:0;width:1200px;height:582px;background:var(--light)}
.services h2{position:absolute;top:58px;width:1200px;text-align:center;font-size:46px}
.grid{position:absolute;left:77px;top:161px;display:grid;grid-template-columns:repeat(6,166px);column-gap:10px;row-gap:15px}
.card{height:171px;background:var(--white);text-align:center;padding-top:17px}
.card.active{box-shadow:0 2px 10px rgba(0,0,0,.12)}
.card svg{width:66px;height:66px;stroke:#333;fill:none;stroke-width:2}
.card.active svg{stroke:var(--rose)}
.card p{margin-top:16px;font-size:14.5px;font-weight:600;line-height:23px;color:var(--ink)}
.card.active p{color:var(--brown)}

/* quote */
.quote{position:absolute;top:1853px;left:0;width:1200px;height:365px;background:var(--brown)}
.quote .portrait{position:absolute;left:125px;top:0;width:313px;height:365px;background:linear-gradient(180deg,#d09d92 0%,#c9978b 55%,#8c8680 100%)}
.quote h2{position:absolute;left:498px;top:80px;font-size:48px;color:var(--white)}
.quote p{position:absolute;left:498px;top:153px;width:610px;font-size:16px;line-height:27px;color:var(--white)}
.quote .btn{position:absolute;left:500px;top:221px}

/* contact */
.contact{position:absolute;top:2218px;left:0;width:1200px;height:470px}
.contact h2{position:absolute;top:58px;width:1200px;text-align:center;font-size:48px}
.contact .sub{position:absolute;top:129px;width:1200px;text-align:center;font-size:16px;color:var(--muted)}
.field{position:absolute;background:var(--field);font-size:13px;color:#777;padding:17px 16px}
.field.focus{background:var(--white);border:1px solid var(--rose);color:var(--rose)}
.contact .btn{position:absolute;left:509px;top:357px}

/* footer */
.footer{position:absolute;top:2688px;left:0;width:1200px;height:374px;background:var(--dark);color:var(--white)}
.footer .brand{position:absolute;top:52px;width:1200px;text-align:center;font-family:"Varela Round",sans-serif;font-size:52px}
.footer .circle{position:absolute;left:577px;top:127px;width:46px;height:46px}
.footer .line{position:absolute;left:286px;width:628px;height:1px;background:rgba(255,255,255,.2)}
.footer .item{position:absolute;top:224px;font-size:14px;line-height:23px;color:#ddd}
.footer svg{position:absolute;fill:var(--brown)}
.footer .copy{position:absolute;top:313px;width:1200px;text-align:center;font-size:14px;color:#ddd}
.footer .copy span{color:var(--brown)}
</style>
</head>
<body>

<header class="nav">
  <div class="brand heading">Pelmora</div>
  <ul>
    <li class="active">HOME</li><li>ABOUT</li><li>SERVICES</li><li>MY QUOTE</li><li>CONTACT US</li>
  </ul>
  <span class="circle"></span>
</header>

<section class="hero">
  <div class="photo" role="img" aria-label="Photograph of a businesswoman holding a folder in front of city buildings"></div>
  <div class="rule" style="top:203px"></div>
  <h1>Pelmora</h1>
  <div class="rule" style="top:286px"></div>
  <div class="creds">Mara Kostellou-Vance &nbsp;|&nbsp; MDipl &nbsp; | &nbsp; BIntSt &nbsp; | &nbsp; B.Sc</div>
  <div class="info" style="top:358px"><span>ADDRESS :</span> 418 Harbour Lane, Kerrowby, 0712, Auckland</div>
  <div class="info" style="top:390px;font-size:16px"><span>PHONE :</span> 021 60 37 19</div>
  <div class="info" style="top:425px"><span>EMAIL US :</span> mara@pelmora.co.nz</div>
</section>

<section class="about">
  <div class="band"></div>
  <div class="portrait" role="img" aria-label="Portrait photograph of the founder"></div>
  <h2 class="heading">About Pelmora</h2>
  <p class="lead">I come from Greece where I completed my Bachelor in Political Science and International Studies. I continued my studies in UK, in Birmingham where I received a Master's Degree in Diplomacy.</p>
  <p class="body" style="top:263px">Further education includes Jo Varnell courses, Board Leaders Institute governance courses, University of Kerrowby Contract's Law and a 2017 Ashfield University paper on 'Disruptive Strategy'.</p>
  <p class="body" style="top:363px">I worked at the HARBOUR 2004 Organising Committee for the Summer and Para Games in 2001 looking after the National Para Sport Committees as the Deputy Manager in the International Relations Department.</p>
  <span class="btn">CONTACT US</span>
</section>

<section class="services">
  <h2 class="heading">Our Services</h2>
  <div class="grid">
    <div class="card"><svg viewBox="0 0 66 66"><rect x="15" y="4" width="36" height="22" rx="2"/><circle cx="33" cy="15" r="5"/><path d="M4 30v18l12 14M62 30v18L50 62M12 42l8 8M54 42l-8 8"/></svg><p>Fundraising Strategic<br>Action Plans</p></div>
    <div class="card active"><svg viewBox="0 0 66 66"><rect x="8" y="18" width="50" height="34" rx="2"/><path d="M2 56h62M28 30l10 5-10 5z"/><path d="M40 6l10 8-10 4z"/></svg><p>Marketing<br>Plans</p></div>
    <div class="card"><svg viewBox="0 0 66 66"><path d="M14 2h28l12 12v50H14z"/><path d="M42 2v12h12M22 40h24M22 46h24M22 52h24M22 58h24"/><path d="M34 10v22M38 14h-6a3 3 0 0 0 0 6h4a3 3 0 0 1 0 6h-8"/></svg><p>Workshops On<br>Fundraising</p></div>
    <div class="card"><svg viewBox="0 0 66 66"><circle cx="22" cy="20" r="10"/><path d="M4 64c0-14 8-22 18-22s18 8 18 22"/><rect x="38" y="4" width="24" height="32"/><path d="M42 28l6-6 4 4 6-8"/></svg><p>Evaluation on<br>Fundraising Projects</p></div>
    <div class="card"><svg viewBox="0 0 66 66"><rect x="14" y="2" width="38" height="62" rx="4"/><path d="M14 12h38M14 54h38"/><rect x="20" y="18" width="7" height="7"/><rect x="30" y="18" width="7" height="7"/><rect x="40" y="18" width="7" height="7"/><rect x="20" y="30" width="7" height="7"/><rect x="30" y="30" width="7" height="7"/><rect x="40" y="30" width="7" height="7"/><rect x="20" y="42" width="7" height="7"/><rect x="30" y="42" width="7" height="7"/></svg><p>Funding<br>Applications</p></div>
    <div class="card"><svg viewBox="0 0 66 66"><rect x="2" y="4" width="62" height="10"/><rect x="6" y="14" width="54" height="48"/><path d="M12 40l14-12 14 12M16 38v20h20V38M44 24l12 12"/><circle cx="46" cy="26" r="2"/><circle cx="54" cy="34" r="2"/></svg><p>Commercial<br>Partnerships</p></div>
    <div class="card"><svg viewBox="0 0 66 66"><rect x="6" y="4" width="20" height="14"/><path d="M26 10h12l4 6-8 4M6 46h14l10 6h22l10-10M4 44v20"/><circle cx="32" cy="34" r="6"/></svg><p>Giving<br>Programmes</p></div>
    <div class="card"><svg viewBox="0 0 66 66"><path d="M10 2h34v24M10 2v42h18"/><path d="M16 10h22M16 16h22M16 22h16"/><path d="M4 50l12-12 18 6 14-8 14 10-18 14H20z"/><path d="M44 22l8-6 8 6-8 10z"/></svg><p>Legacy<br>Programmes</p></div>
    <div class="card"><svg viewBox="0 0 66 66"><circle cx="26" cy="26" r="20"/><path d="M6 26h40M26 6c-8 8-8 32 0 40M26 6c8 8 8 32 0 40"/><circle cx="42" cy="42" r="8"/><path d="M48 48l12 12"/></svg><p>Capital Projects<br>Fundraising</p></div>
    <div class="card"><svg viewBox="0 0 66 66"><rect x="12" y="8" width="42" height="56"/><path d="M18 2v10M26 2v10M34 2v10M42 2v10M48 2v10M20 50h26M20 56h26"/><path d="M33 18v24M38 22h-7a3 3 0 0 0 0 6h4a3 3 0 0 1 0 6h-8"/></svg><p>Feasibility<br>Studies</p></div>
    <div class="card"><svg viewBox="0 0 66 66"><rect x="22" y="2" width="26" height="30" rx="2"/><circle cx="35" cy="18" r="6"/><path d="M30 8h10"/><path d="M2 44h10l10-6h16l-2 6H26M12 44v14l14 4 30-18-4-4-16 6"/></svg><p>Consultancy on<br>Fundraising</p></div>
    <div class="card"><svg viewBox="0 0 66 66"><path d="M30 4h16l-4 8h-8z"/><circle cx="38" cy="30" r="18"/><path d="M38 20v20M42 23h-6a3 3 0 0 0 0 6h4a3 3 0 0 1 0 6h-6"/><path d="M2 50h10l10-4h10M2 62h22l22-8"/></svg><p>Mentoring on<br>Fundraising</p></div>
  </div>
</section>

<section class="quote">
  <div class="portrait" role="img" aria-label="Photograph of a smiling young woman holding a phone"></div>
  <h2 class="heading">My Quote</h2>
  <p>I look forward to working with you and your team andtogether achieving results that will make a difference where we live.</p>
  <span class="btn">CONTACT US</span>
</section>

<section class="contact">
  <h2 class="heading">Contact Us</h2>
  <p class="sub">If you have an any Question for contact us Today !</p>
  <div class="field focus" style="left:174px;top:175px;width:271px;height:52px">Name *</div>
  <div class="field" style="left:454px;top:175px;width:271px;height:52px">Emial *</div>
  <div class="field" style="left:735px;top:175px;width:271px;height:52px">Phone *</div>
  <div class="field" style="left:174px;top:238px;width:832px;height:104px">Message *</div>
  <span class="btn">SUBMIT</span>
</section>

<footer class="footer">
  <div class="brand">Pelmora</div>
  <span class="circle"></span>
  <div class="line" style="top:195px"></div>
  <svg style="left:320px;top:232px" width="18" height="26" viewBox="0 0 18 26"><path d="M9 0a9 9 0 0 0-9 9c0 7 9 17 9 17s9-10 9-17a9 9 0 0 0-9-9zm0 13a4 4 0 1 1 0-8 4 4 0 0 1 0 8z"/></svg>
  <div class="item" style="left:352px">418 Harbour Lane, Kerrowby,<br>0712, Auckland</div>
  <svg style="left:556px;top:227px" width="22" height="22" viewBox="0 0 24 24"><path d="M6.6 10.8a15 15 0 0 0 6.6 6.6l2.2-2.2c.3-.3.7-.4 1-.2 1.1.4 2.3.6 3.6.6.6 0 1 .4 1 1V20c0 .6-.4 1-1 1A17 17 0 0 1 3 4c0-.6.4-1 1-1h3.5c.6 0 1 .4 1 1 0 1.3.2 2.5.6 3.6.1.3 0 .7-.2 1z"/></svg>
  <div class="item" style="left:590px">021 60 37 19</div>
  <svg style="left:717px;top:232px" width="22" height="17" viewBox="0 0 22 17"><path d="M0 0h22v2L11 9 0 2z M0 4l11 7 11-7v13H0z"/></svg>
  <div class="item" style="left:754px;top:227px">mara@pelmora.co.nz</div>
  <div class="line" style="top:270px"></div>
  <p class="copy">©<span>Pelmora</span> - 2019 All Rights Reserved. Privacy | Policy Terms</p>
</footer>

</body>
</html>
```